Redesign This Psychology Website

We would like a slight redesign of this successful psychology (relationship counselling) website:

www.TheWillowNook.com.au

We are updating the website, and we'd like a slight refresh of the design and style.

Please keep to very similar colours, and use the same logo. We're looking for around 10 page templates, however the main one is the home page.

Keep in mind, this website already converts quite well, so we want a new, fresh design in keeping with this one. Please don't bother designing something too extremely different.

thanks :)

Target Market(s)

couples who are looking for relationship counselling. Men and women, 25 - 70, across Australia

Industry/Entity Type

Psychology

Number of Pages Required

5+ page

Font styles to use
Sans Serif

Colors
87cfc6
b7a5cd
ec1f27
ffffff
cee9f5

Requirements
Must have
• a similar look to the current design, just looking for a slight refresh.
• Search bar
• Areas for lots of photos
• same logo
• lots of content areas
Nice to have
• great content areas, where we can display a lot of content and our areas.
Should not have
• no colors like orange, etc.
• should not have a totally different feel.

```html
<!DOCTYPE html>
<html lang="en">
<head>
<meta charset="utf-8">
<title>The Willow Nook — Relationship Counselling</title>
<link href="https://fonts.googleapis.com/css2?family=Lato:wght@300;400;700&display=swap" rel="stylesheet">
<style>
  :root{
    --teal:#1d8a96;
    --teal-dark:#146f7a;
    --teal-soft:#7fc3cc;
    --band-light:#e4f3f8;
    --band-lighter:#f3fafc;
    --coral:#ec5b5e;
    --coral-dark:#e2474c;
    --grey-btn:#b3aeae;
    --grey-text:#8f8f8f;
    --dark-text:#333;
    --line:#cfd3d4;
    --white:#fff;
    --frame:#e3eff3;
  }
  *{margin:0;padding:0;box-sizing:border-box}
  html,body{width:1058px;height:1200px;overflow:hidden;background:var(--white);
    font-family:'Lato',sans-serif;color:var(--dark-text)}
  .page{position:relative;width:1058px;height:1200px}
  .abs{position:absolute}

  /* header */
  .brand{left:127px;top:17px;display:flex;align-items:center;gap:8px}
  .brand-dot{width:34px;height:34px;border-radius:50%;background:var(--teal)}
  .brand-name{font-size:23px;font-weight:400;color:var(--teal);line-height:1}
  .brand-tag{font-size:9px;font-weight:700;color:var(--teal);margin-top:4px}
  .call{left:469px;top:16px;font-size:28px;font-weight:300;color:var(--teal-soft)}
  .call strong{font-weight:700;color:var(--teal)}
  .social{left:802px;top:20px;display:flex;align-items:center;gap:8px}
  .social-label{font-size:10px;line-height:11px;color:#b9c9cc;margin-right:6px}
  .social-box{width:20px;height:20px;background:var(--teal-soft)}

  .nav{left:130px;top:84px;font-size:13px;letter-spacing:1px;color:#6d6d6d}
  .nav span{position:absolute;white-space:nowrap}
  .nav .active{color:#e8262c;font-weight:700}
  .search-line{left:739px;top:80px;width:188px;height:20px;border-bottom:1px solid var(--line)}

  .subnav{left:122px;top:114px;width:814px;height:49px;
    background:linear-gradient(90deg,var(--band-light),var(--band-lighter));}
  .subnav span{position:absolute;top:0;height:49px;display:flex;align-items:center;justify-content:center;
    text-align:center;font-size:13px;line-height:14px;color:var(--teal)}
  .subnav .current{left:0;width:131px;background:var(--coral);color:var(--white)}

  .hero{left:122px;top:171px;width:814px;height:321px;
    background:linear-gradient(100deg,#8c9ea4 0%,#7e6a58 35%,#5b3b2a 60%,#8f4b3a 78%,#3b2520 100%)}
  .play{left:220px;top:277px;width:100px;height:72px;border-radius:16px;background:rgba(255,255,255,.22)}
  .play svg{position:absolute;left:40px;top:24px}
  .play-text{left:312px;top:262px;font-size:50px;font-weight:300;color:var(--white);line-height:45px;letter-spacing:2px}
  .badge{left:834px;top:171px;width:102px;height:80px;background:var(--white);
    clip-path:polygon(0 0,100% 0,100% 100%,30% 100%)}
  .badge-mark{left:880px;top:187px;width:36px;height:36px;border-radius:50%;background:#1a6fa8}

  /* services */
  .feature-frame{left:315px;top:538px;width:213px;height:459px;border:3px solid var(--frame)}
  .service{top:0;width:190px;text-align:center}
  .service h2{position:absolute;left:0;width:190px;top:572px;font-size:18px;font-weight:300;
    letter-spacing:1px;line-height:18px;color:var(--teal)}
  .service.featured h2{font-weight:700;color:var(--teal)}
  .service .ask{position:absolute;left:0;width:190px;top:644px;font-size:13px;color:var(--dark-text)}
  .service .list{position:absolute;left:0;width:190px;top:668px;font-size:11px;line-height:14.5px;color:var(--grey-text)}
  .photo{position:absolute;left:24px;top:756px;width:142px;height:142px;border-radius:50%;
    background:radial-gradient(circle at 50% 40%,#e9dfd6,#b9aea6);box-shadow:0 2px 8px rgba(0,0,0,.18);
    border:4px solid var(--white)}
  .btn{position:absolute;left:0;width:174px;top:929px;height:30px;display:flex;align-items:center;justify-content:center;
    font-size:12px;color:var(--white);background:linear-gradient(#c4bfbf,var(--grey-btn));box-shadow:0 1px 2px rgba(0,0,0,.2)}
  .featured .btn{background:var(--coral)}
  .more{position:absolute;left:0;top:970px;width:174px;display:flex;align-items:center;gap:14px;
    font-size:12px;color:#888;letter-spacing:.5px}
  .more i{flex:1;height:1px;background:var(--line)}

  /* finder */
  .finder{left:121px;top:1029px;width:814px;height:126px;
    background:linear-gradient(100deg,#7ec2cb,#4da3b2);box-shadow:0 2px 12px rgba(80,160,180,.35)}
  .finder-title{left:153px;top:1052px;font-size:22px;line-height:24px;color:var(--white);font-weight:300}
  .finder-title b{font-weight:700}
  .label{top:1066px;font-size:13px;color:#d9f0f3}
  .field{top:1090px;height:33px;border:1px solid #d6eef2;display:flex;align-items:center;
    padding-left:12px;font-size:12px;color:var(--white)}
  .select-arrow{position:absolute;right:0;top:0;width:32px;height:31px;border-left:1px solid #d6eef2;
    display:flex;align-items:center;justify-content:center}
  .search-btn{left:810px;top:1090px;width:96px;height:33px;background:var(--coral);color:var(--white);
    font-size:12px;display:flex;align-items:center;justify-content:center}
</style>
</head>
<body>
<div class="page">

  <div class="abs brand">
    <div class="brand-dot"></div>
    <div>
      <div class="brand-name">The Willow Nook</div>
      <div class="brand-tag">helping you create loving relationships</div>
    </div>
  </div>
  <div class="abs call">Call us on <strong>1300 555 014</strong></div>
  <div class="abs social">
    <div class="social-label">social<br>media</div>
    <div class="social-box"></div><div class="social-box"></div><div class="social-box"></div>
  </div>

  <nav class="abs nav">
    <span class="active" style="left:0">HOME</span>
    <span style="left:78px">ABOUT</span>
    <span style="left:165px">RESOURCES</span>
    <span style="left:283px">BLOG</span>
    <span style="left:356px">SHOP</span>
    <span style="left:427px">CART</span>
    <span style="left:497px">SEARCH</span>
  </nav>
  <div class="abs search-line">
    <svg width="13" height="13" viewBox="0 0 13 13"><circle cx="5.5" cy="5.5" r="4" fill="none" stroke="#1d8a96" stroke-width="1.6"/><line x1="8.5" y1="8.5" x2="12" y2="12" stroke="#1d8a96" stroke-width="1.6"/></svg>
  </div>

  <div class="abs subnav">
    <span class="current">COUNSELLING<br>TYPES</span>
    <span style="left:140px;width:200px">RELATIONSHIP COUNSELLING<br>LOCATIONS</span>
    <span style="left:350px;width:140px">SEX THERAPY<br>LOCATIONS</span>
    <span style="left:500px;width:80px">QUIZZES</span>
    <span style="left:597px;width:80px">F.A.Q.'S</span>
    <span style="left:705px;width:100px">CONTACT</span>
  </div>

  <div class="abs hero" role="img" aria-label="Smiling woman holding flowers on a coastal cliff at sunset"></div>
  <div class="abs play"><svg width="22" height="24" viewBox="0 0 22 24"><polygon points="0,0 22,12 0,24" fill="#3a2a24"/></svg></div>
  <div class="abs play-text">PLAY<br>VIDEO</div>
  <div class="abs badge"></div>
  <div class="abs badge-mark"></div>

  <div class="abs feature-frame"></div>

  <section class="abs service" style="left:115px">
    <h2>RELATIONSHIP<br>COUNSELLING</h2>
    <p class="ask">Do you need help with:</p>
    <p class="list">Communication, Recovering<br>from an affair, Loss of<br>intimacy &amp; love, Power<br>battles, Feeling like friends,<br>not lovers</p>
    <div class="photo" role="img" aria-label="Young couple standing together"></div>
    <a class="btn" style="left:8px">TAKE OUR SEX QUIZ</a>
    <div class="more" style="left:8px">MORE<i></i></div>
  </section>

  <section class="abs service featured" style="left:327px">
    <h2>SEX THERAPY<br>COUNSELLING</h2>
    <p class="ask">Do you need help with:</p>
    <p class="list">Low libido , Erectile difficulties,<br>Premature ejaculation, Differing<br>libidos, Porn addiction,<br>Keeping sex exciting</p>
    <div class="photo" role="img" aria-label="Smiling older couple lying together"></div>
    <a class="btn" style="left:9px">TAKE OUR SEX QUIZ</a>
    <div class="more" style="left:11px">MORE<i></i></div>
  </section>

  <section class="abs service" style="left:535px">
    <h2 style="top:571px">ANGER<br>MANAGEMENT<br>COUNSELLING</h2>
    <p class="ask">Do you need help with:</p>
    <p class="list">Managing angry outbursts,<br>expressing your anger<br>in healthy ways</p>
    <div class="photo" role="img" aria-label="Frowning man with arms crossed"></div>
    <a class="btn" style="left:9px;top:927px">TAKE OUR SEX QUIZ</a>
    <div class="more" style="left:10px">MORE<i></i></div>
  </section>

  <section class="abs service" style="left:751px">
    <h2 style="top:570px">NARCISSISM<br>COUNSELLING</h2>
    <p class="ask">Do you need help with:</p>
    <p class="list">Managing narcissistic, superior,<br>entitled, arrogant and lack of<br>empathy tendencies in<br>you or your partner</p>
    <div class="photo" role="img" aria-label="Woman holding a yellow flower"></div>
    <a class="btn" style="left:7px;top:926px">TAKE OUR SEX QUIZ</a>
    <div class="more" style="left:7px">MORE<i></i></div>
  </section>

  <div class="abs finder"></div>
  <div class="abs finder-title"><b>Find Our</b><br>Psychologist<br>Near You</div>
  <div class="abs label" style="left:320px">Type of Counselling</div>
  <div class="abs label" style="left:530px">Location</div>
  <div class="abs label" style="left:694px">Postcode</div>
  <div class="abs field" style="left:320px;width:192px">relationship counselling
    <span class="select-arrow"><svg width="12" height="7" viewBox="0 0 12 7"><polyline points="1,1 6,6 11,1" fill="none" stroke="#fff" stroke-width="1.3"/></svg></span>
  </div>
  <div class="abs field" style="left:530px;width:144px">New York</div>
  <div class="abs field" style="left:694px;width:96px">56-994</div>
  <div class="abs search-btn">SEARCH</div>

</div>
</body>
</html>
```